tamo rix

TAMO RIX mobile technology servicesPhone and tablet repairs, screens data recovery.

Industry/Entity Type

Data Recovery

Contact Information for Business Card

0431 587 612

Colors
33a6d7
f04a50
0a90cc
e34197

Requirements
Must have
• Gary plinth
Nice to have
• White background

```html
<!DOCTYPE html>
<html lang="en">
<head>
<meta charset="utf-8">
<title>Gary plinth – TAMO RIX</title>
<link href="https://fonts.googleapis.com/css2?family=Lato:wght@400;700&display=swap" rel="stylesheet">
<style>
  :root {
    --brand-blue: #33a6d7;
    --brand-red: #f04a50;
    --deep-blue: #0a90cc;
    --page: #ffffff;
    --panel: #fafafa;
    --rule: #d6d6d6;
    --white: #ffffff;
  }
  * { box-sizing: border-box; margin: 0; padding: 0; }
  html, body {
    width: 1200px;
    height: 720px;
    overflow: hidden;
    background: var(--page);
    font-family: "Lato", Arial, sans-serif;
  }
  .business-card {
    position: absolute;
    left: 40px;
    top: 40px;
    width: 1115px;
    height: 625px;
    border-radius: 22px;
    overflow: hidden;
    background: var(--panel);
  }
  .card-top {
    position: relative;
    height: 395px;
    background: linear-gradient(150deg, #ffffff 0%, var(--panel) 45%, #f7f7f7 100%);
  }
  .brand-block {
    position: absolute;
    left: 0;
    top: 0;
    width: 512px;
    height: 395px;
    display: flex;
    align-items: center;
    justify-content: center;
    gap: 20px;
  }
  .brand-dot {
    width: 64px;
    height: 64px;
    border: 7px solid var(--brand-blue);
    border-radius: 50%;
  }
  .brand-name {
    color: var(--brand-blue);
    font-weight: 700;
    font-size: 44px;
    letter-spacing: 1px;
  }
  .divider {
    position: absolute;
    left: 512px;
    top: 32px;
    width: 1px;
    height: 330px;
    background: var(--rule);
  }
  .contact-block {
    position: absolute;
    left: 570px;
    top: 140px;
  }
  .person-name {
    color: var(--brand-blue);
    font-weight: 700;
    font-size: 52px;
    line-height: 1;
  }
  .phone-line {
    display: flex;
    align-items: center;
    gap: 12px;
    margin-top: 12px;
    color: var(--brand-red);
    font-size: 26px;
  }
  .phone-line svg { width: 42px; height: 42px; }
  .card-bottom {
    height: 230px;
    background: var(--brand-blue);
    display: flex;
  }
  .service {
    flex: 1;
    display: flex;
    flex-direction: column;
    align-items: center;
    padding-top: 48px;
    color: var(--white);
    font-size: 25px;
    text-transform: uppercase;
  }
  .service svg { width: 104px; height: 104px; margin-bottom: 22px; }
</style>
</head>
<body>
  <main class="business-card">
    <section class="card-top">
      <div class="brand-block">
        <span class="brand-dot"></span>
        <span class="brand-name">TAMO RIX</span>
      </div>
      <div class="divider"></div>
      <div class="contact-block">
        <h1 class="person-name">Gary plinth</h1>
        <p class="phone-line">
          <svg viewBox="0 0 42 42" aria-hidden="true">
            <circle cx="21" cy="21" r="19" fill="none" stroke="var(--brand-red)" stroke-width="2.5"/>
            <path d="M14 11c1-1 2-1 3 0l2.5 3.5c.7 1 .5 2-.3 2.7l-1.5 1.3c1 2.5 3 4.6 5.5 5.7l1.4-1.5c.7-.8 1.8-1 2.7-.3L30.8 25c1 1 1 2 0 3l-1.8 1.8c-1.6 1.6-4.3 1.3-7.3-.6-3.5-2.2-6.6-5.5-8.4-9-1.5-3-1.6-5.7-.1-7.2z" fill="var(--brand-red)"/>
          </svg>
          <span>0431 587 612</span>
        </p>
      </div>
    </section>
    <section class="card-bottom">
      <div class="service">
        <svg viewBox="0 0 104 104" aria-hidden="true">
          <circle cx="52" cy="52" r="48" fill="none" stroke="var(--white)" stroke-width="4"/>
          <rect x="33" y="27" width="38" height="50" rx="5" fill="var(--white)"/>
          <rect x="37" y="31" width="30" height="38" fill="var(--brand-blue)"/>
          <circle cx="52" cy="73" r="2" fill="var(--brand-blue)"/>
        </svg>
        <span>Phone and tablet repairs</span>
      </div>
      <div class="service">
        <svg viewBox="0 0 104 104" aria-hidden="true">
          <circle cx="52" cy="52" r="48" fill="none" stroke="var(--white)" stroke-width="4"/>
          <path d="M32 48a20 20 0 0 1 35-10" fill="none" stroke="var(--white)" stroke-width="8"/>
          <path d="M74 28v18H56z" fill="var(--white)"/>
          <path d="M72 56a20 20 0 0 1-35 10" fill="none" stroke="var(--white)" stroke-width="8"/>
          <path d="M30 76V58h18z" fill="var(--white)"/>
        </svg>
        <span>Screens data recovery</span>
      </div>
    </section>
  </main>
</body>
</html>
```